New business card for KT4 Linkway, a marketing company.

We need a new business card design. We would like it to be blue gray and white. We would like some movement but in a more subtle pattern than in the file we uploaded. We are a marketing company that connects brands with their target audiences - we make connections. We work in the New York Metro area with sophisticated clients. The card should feel modern, upscale and professional.

Target Market(s)

Businesses looking to grow their brands in tourism and nightlife. We work with liquor and beer companies and with Tourism bureaus and companies.

Industry/Entity Type

Marketing

Contact Information for Business Card

Would like a horizontal layout, two-sided. Would like the logo on the back with the tagline ' "connecting brands to their target audiences" under the logo. On the front, we would like name, title, contact email, contact phone, website.

Font styles to use
Sans Serif

Colors
3377b5
85cae6
ffffff

Requirements
Must have
• Our logo. See attached. Otherwise, open to your ideas.
Should not have
• No colors we don't want - no reds/pinks/oranges please

```html
<!DOCTYPE html>
<html lang="en">
<head>
<meta charset="UTF-8">
<title>KT4 Linkway – Business Card</title>
<link rel="stylesheet" href="https://fonts.googleapis.com/css2?family=Questrial&family=Michroma&display=swap">
<style>
  :root {
    --brand-blue: #3377b5;
    --brand-blue-soft: #4a88c0;
    --brand-gray: #8a8c8f;
    --paper: #ffffff;
    --backdrop: #e4e6e8;
    --title-gray: #7f9ab3;
    --card-w: 900px;
    --card-h: 514px;
  }
  * { box-sizing: border-box; margin: 0; padding: 0; }
  html, body {
    width: 1200px;
    height: 1200px;
    overflow: hidden;
    background: var(--backdrop);
  }
  .canvas {
    width: 1200px;
    height: 1200px;
    display: flex;
    flex-direction: column;
    align-items: center;
    justify-content: center;
    gap: 60px;
  }
  .card {
    position: relative;
    width: var(--card-w);
    height: var(--card-h);
    background: var(--paper);
    overflow: hidden;
    box-shadow: 0 6px 18px rgba(0,0,0,0.12);
    font-family: "Questrial", sans-serif;
  }
  .pattern-band {
    position: absolute;
    left: 0;
    right: 0;
    top: 290px;
    bottom: 0;
    background: linear-gradient(170deg, var(--brand-gray) 0%, var(--brand-blue) 22%, var(--brand-blue-soft) 100%);
  }
  .wordmark {
    position: absolute;
    color: var(--brand-blue);
    font-family: "Questrial", sans-serif;
    text-transform: uppercase;
    white-space: nowrap;
  }
  .front .wordmark {
    left: 60px;
    top: 120px;
    font-size: 38px;
    letter-spacing: 1px;
  }
  .holder {
    position: absolute;
    right: 60px;
    top: 62px;
    text-align: left;
  }
  .holder-name {
    font-family: "Michroma", sans-serif;
    font-size: 25px;
    color: var(--brand-blue);
    letter-spacing: 0.5px;
  }
  .holder-title {
    font-size: 14px;
    color: var(--title-gray);
    letter-spacing: 1px;
    margin-top: 4px;
  }
  .contact {
    position: absolute;
    right: 60px;
    top: 318px;
    text-align: right;
    color: var(--paper);
    font-size: 17px;
    line-height: 1.6;
    letter-spacing: 0.5px;
  }
  .address {
    position: absolute;
    left: 90px;
    bottom: 48px;
    color: var(--paper);
    font-size: 18px;
    line-height: 1.5;
    letter-spacing: 1px;
  }
  .address span { display: block; }
  .address span + span { padding-left: 60px; }

  .back {
    display: flex;
    flex-direction: column;
    align-items: center;
    justify-content: center;
    gap: 30px;
  }
  .back .wordmark {
    position: static;
    font-size: 66px;
    letter-spacing: 2px;
  }
  .tagline {
    color: var(--brand-blue);
    font-size: 19px;
    letter-spacing: 1.5px;
    text-transform: uppercase;
  }
</style>
</head>
<body>
<main class="canvas">

  <section class="card front" aria-label="Business card front">
    <div class="pattern-band" role="img" aria-label="Decorative flowing pattern in blue and gray"></div>

    <p class="wordmark">KT4 Linkway</p>

    <div class="holder">
      <p class="holder-name">YOUR GOOD NAME</p>
      <p class="holder-title">TITLE</p>
    </div>

    <div class="contact">
      <p>hello@kt4linkway.com</p>
      <p>212-555-0148</p>
      <p>kt4linkway.com</p>
    </div>

    <p class="address">
      <span>Harlow Lane, 48, suite#310</span>
      <span>New York NY, 10021.</span>
    </p>
  </section>

  <section class="card back" aria-label="Business card back">
    <p class="wordmark">KT4 Linkway</p>
    <p class="tagline">Connecting brands to their target audiences</p>
  </section>

</main>
</body>
</html>
```